Velmar Intergrated Marketing Stationary Design Contest

We require a very professional looking stationary set to include: letterhead, compliments slip and business cards (double sided bus cards).

Files should be supplied on either Illustrator or InDesign.

We are interested in perhaps encorporating a faint watermark with the letter q or the logo, but it isnt a pre-requisite

Target Market(s)

Business owners seeking professional marketing services

Industry/Entity Type

Marketing

Requirements
Must have
• Concurrent theme wiht business cards, letterhead and comp slip. Must be an editable document for future ammendment
Should not have
• No use of times new roman or similar fonts

```html
<!DOCTYPE html>
<html lang="en">
<head>
<meta charset="utf-8">
<title>Velmar Integrated Marketing – Stationery Set</title>
<link rel="stylesheet" href="https://fonts.googleapis.com/css2?family=Mulish:wght@400;600;700&display=swap">
<style>
:root{
  --brand-red:#ff3515;
  --brand-red-soft:rgba(255,53,21,.18);
  --ink:#111111;
  --text-grey:#555555;
  --rule-grey:#8a8a8a;
  --card-grey:#b2b2b2;
  --paper:#ffffff;
}
*{margin:0;padding:0;box-sizing:border-box}
html,body{width:1200px;height:1128px;overflow:hidden;background:var(--paper)}
body{position:relative;font-family:"Mulish",sans-serif;color:var(--text-grey)}

/* brand name lockup */
.brand{position:absolute;display:flex;align-items:center;gap:.35em;font-weight:600;color:var(--ink);letter-spacing:.12em;white-space:nowrap}
.brand .dot{width:.9em;height:.9em;border-radius:50%;background:var(--brand-red);flex:none}
.brand span{line-height:1}
.brand small{display:block;font-size:.3em;letter-spacing:.18em;margin-top:.25em}
.masthead{left:468px;top:10px;font-size:62px}

/* sheets */
.sheet{position:absolute;background:var(--paper);border:1px solid var(--rule-grey);box-shadow:3px 3px 4px rgba(0,0,0,.25);overflow:hidden}
.letterhead{left:267px;top:177px;width:674px;height:945px}
.comp-slip{left:112px;top:544px;width:674px;height:315px}
.sheet .brand{font-size:21px;left:34px;top:52px}

/* accent field where the brand sweep sits */
.accent-field{position:absolute;background:linear-gradient(100deg,var(--brand-red) 0%,var(--brand-red-soft) 100%)}
.letterhead .accent-field,.comp-slip .accent-field{left:0;top:200px;width:380px;height:92px}

.office{position:absolute;left:480px;top:16px;padding-left:14px;border-left:1px solid var(--rule-grey);height:105px;padding-top:15px;font-size:7.6px;line-height:9.4px}
.office strong{font-weight:700;color:#333}
.office p+p{margin-top:9px}

.company-footer{position:absolute;left:0;right:0;top:896px;display:flex;justify-content:center;gap:46px;font-size:7.6px}

/* business cards */
.card{width:289px;height:159px;left:855px}
.card-front{top:328px}
.card-back{top:500px;background:var(--card-grey)}
.card-alt-front{top:704px}
.card-alt-back{top:877px}
.card .brand{font-size:19px}
.card-front .brand{left:16px;top:20px}
.card-back .brand{left:86px;top:64px;color:var(--paper)}
.card-back .brand .dot{background:var(--paper)}
.card-alt-front .brand{left:168px;top:66px}
.card-alt-back .brand{left:160px;top:64px}
.card-alt-front .accent-field{left:0;top:0;width:50px;height:159px}
.card-alt-back .accent-field{right:0;top:0;width:110px;height:159px;background:linear-gradient(180deg,var(--brand-red) 0%,var(--brand-red-soft) 100%)}

.person{position:absolute;font-size:7.6px;line-height:9.4px}
.person h2{font-size:9.5px;font-weight:700;color:#333;line-height:10px}
.person .role{margin-top:0}
.person p+p{margin-top:9px}
.card-front .person{left:168px;top:30px}
.card-alt-front .person{left:61px;top:24px}
</style>
</head>
<body>

<div class="brand masthead"><i class="dot"></i><span>velmar<small>Integrated Marketing</small></span></div>

<section class="sheet letterhead">
  <div class="accent-field" role="img" aria-label="Red brand sweep sweeping across the sheet"></div>
  <div class="brand"><i class="dot"></i><span>velmar<small>Integrated Marketing</small></span></div>
  <div class="office">
    <p><strong>Velmar Integrated Marketing Central Offices</strong><br>Mill Lane, Hebden<br>West Riding, HX7 4QT</p>
    <p>www.velmarim.co.uk<br>enquiries@velmarim.co.uk<br>T 01632 960414<br>F 01632 960411</p>
  </div>
  <footer class="company-footer">
    <span>Company registration 4815162</span><span>Vat No 718 2043 55</span><span>Trading as a division of Brookfield Ltd</span>
  </footer>
</section>

<section class="sheet comp-slip">
  <div class="accent-field" role="img" aria-label="Red brand sweep sweeping across the slip"></div>
  <div class="brand"><i class="dot"></i><span>velmar<small>Integrated Marketing</small></span></div>
  <div class="office">
    <p><strong>Velmar Integrated Marketing Central Offices</strong><br>Mill Lane, Hebden<br>West Riding, HX7 4QT</p>
    <p>www.velmarim.co.uk<br>enquiries@velmarim.co.uk<br>T 01632 960414<br>F 01632 960411</p>
  </div>
</section>

<section class="sheet card card-front">
  <div class="brand"><i class="dot"></i><span>velmar<small>Integrated Marketing</small></span></div>
  <div class="person">
    <h2>Rowan Pryce</h2><p class="role">General Manager</p>
    <p>Velmar Integrated Marketing<br>Central Offices<br>Mill Lane, Hebden<br>West Riding, HX7 4QT</p>
    <p>www.velmarim.co.uk<br>rowan@velmarim.co.uk<br>T 01632 960414<br>F 01632 960411</p>
  </div>
</section>

<section class="sheet card card-back">
  <div class="brand"><i class="dot"></i><span>velmar<small>Integrated Marketing</small></span></div>
</section>

<section class="sheet card card-alt-front">
  <div class="accent-field" role="img" aria-label="Red brand accent along the card edge"></div>
  <div class="person">
    <h2>Rowan Pryce</h2><p class="role">General Manager</p>
    <p>Velmar Integrated Marketing<br>Central Offices<br>Mill Lane, Hebden<br>West Riding, HX7 4QT</p>
    <p>www.velmarim.co.uk<br>rowan@velmarim.co.uk<br>T 01632 960414<br>F 01632 960411</p>
  </div>
  <div class="brand"><i class="dot"></i><span>velmar<small>Integrated Marketing</small></span></div>
</section>

<section class="sheet card card-alt-back">
  <div class="accent-field" role="img" aria-label="Red brand accent on the card's right side"></div>
  <div class="brand"><i class="dot"></i><span>velmar<small>Integrated Marketing</small></span></div>
</section>

</body>
</html>
```